Mobile App Design Needed for Medical Activity Tracker

We are looking for a few pages of a mobile app mocked up that will fit with our brand. The app is linked to a smartwatch that tests and tracks blood glucose/ketones. The smartwatch also tracks daily activities such as; sleep, steps, heart-rate, calories burned, time exercising, etc.

You can view our current watch design from the uploaded files. We would like you to stay AROUND this type of color scheme (blue/black). We have also uploaded the current logo.

If you are awarded this job we will also give you first go at designing a new watch display as well as completing a Full Mobile App Design.

We would like to see the following app pages designed;
1.) Login page (include options to login with Plinkora.)
2.) Activity Tracking page
3.) Keto Testing page
3a.) Test in progress page
3b.) Test complete page

Target Market(s)

Wearables, Diabetes, ketogenic diet, fitness, smartwatch

Industry/Entity Type

Fitness

Font styles to use
Sans Serif

Colors
33a6d7

Requirements
Must have
• Must have designs for all pages listed in description.
• Contrasting colors.
• Graphs.
• Modern design
Nice to have
• I have added some images of app designs we like.

```html
<!DOCTYPE html>
<html lang="en">
<head>
<meta charset="utf-8">
<title>Keto Levels</title>
<link href="https://fonts.googleapis.com/css2?family=Montserrat:wght@400;500;600;700&display=swap" rel="stylesheet">
<style>
  :root {
    --bg-deep: #0f1624;
    --bg-mid: #1b2738;
    --bg-warm: #243447;
    --nav-bg: #07090d;
    --white: #ffffff;
    --text-soft: #e6ebf2;
    --text-muted: #c9d1dc;
    --rule: rgba(255,255,255,0.28);
    --accent: #33a6d7;
    --accent-bright: #3db3ee;
    --bar-top: #17c3e8;
    --bar-bottom: #1d8fcf;
    --icon-grey: #b9bec6;
  }
  * { margin: 0; padding: 0; box-sizing: border-box; }
  html, body { width: 675px; height: 1200px; overflow: hidden; background: var(--bg-deep); }
  body { font-family: "Montserrat", Arial, sans-serif; color: var(--white); }

  .screen {
    position: relative;
    width: 750px; height: 1334px;
    transform: scale(0.9); transform-origin: 0 0;
    overflow: hidden;
  }
  .backdrop {
    position: absolute; inset: 0;
    background:
      radial-gradient(ellipse 60% 45% at 50% 38%, var(--bg-warm) 0%, rgba(36,52,71,0) 70%),
      linear-gradient(180deg, var(--bg-deep) 0%, var(--bg-mid) 55%, #161f2c 100%);
  }

  .status-bar { position: absolute; top: 0; left: 0; right: 0; height: 44px; font-size: 22px; font-weight: 500; }
  .status-left { position: absolute; left: 10px; top: 9px; display: flex; align-items: center; gap: 8px; }
  .status-time { position: absolute; left: 0; right: 0; top: 10px; text-align: center; font-weight: 600; }
  .status-right { position: absolute; right: 14px; top: 9px; display: flex; align-items: center; gap: 8px; }

  .header-title {
    position: absolute; top: 76px; left: 0; right: 0; text-align: center;
    font-size: 25px; font-weight: 600; letter-spacing: 7px;
  }
  .header-icons { position: absolute; top: 75px; right: 22px; display: flex; gap: 24px; align-items: center; }

  .month-picker {
    position: absolute; left: 270px; top: 145px; width: 202px; height: 61px;
    background: var(--white); border-radius: 31px; color: #111;
    display: flex; align-items: center; justify-content: center; gap: 14px;
    font-size: 23px; font-weight: 500;
  }

  .chart { position: absolute; left: 0; top: 240px; }

  .latest-row {
    position: absolute; left: 34px; right: 0; top: 685px; height: 126px;
    border-top: 1px solid var(--rule); border-bottom: 1px solid var(--rule);
    display: flex; align-items: center;
  }
  .latest-label { margin-left: 55px; font-size: 22px; font-weight: 500; letter-spacing: 2.5px; color: var(--text-soft); }
  .latest-value { position: absolute; right: 30px; font-size: 26px; font-weight: 700; letter-spacing: 1px; color: var(--accent-bright); }
  .drop-icon { position: absolute; left: 4px; top: 46px; }

  .start-test { position: absolute; left: 256px; top: 873px; width: 240px; height: 240px; }
  .start-label {
    position: absolute; top: 1146px; left: 0; right: 0; text-align: center;
    font-size: 25px; font-weight: 600; letter-spacing: 6px;
  }

  .tab-bar {
    position: absolute; left: 0; right: 0; bottom: 0; height: 90px;
    background: var(--nav-bg); display: flex;
  }
  .tab { flex: 1; display: flex; flex-direction: column; align-items: center; padding-top: 16px; gap: 4px; font-size: 18px; font-weight: 600; color: var(--white); }
  .tab svg { width: 34px; height: 34px; }
  .tab.is-active { color: var(--accent-bright); }
</style>
</head>
<body>
<div class="screen">
  <div class="backdrop" role="img" aria-label="Blurred photo of a runner's sneaker on a dark blue background"></div>

  <div class="status-bar">
    <div class="status-left">
      <svg width="34" height="16" viewBox="0 0 34 16" fill="#fff"><rect x="0" y="10" width="5" height="6" rx="1"/><rect x="8" y="7" width="5" height="9" rx="1"/><rect x="16" y="3" width="5" height="13" rx="1"/><rect x="24" y="0" width="5" height="16" rx="1"/></svg>
      <span>Veltro</span>
      <svg width="28" height="20" viewBox="0 0 28 20" fill="none" stroke="#fff" stroke-width="3" stroke-linecap="round"><path d="M2 7a17 17 0 0 1 24 0"/><path d="M7 12a10 10 0 0 1 14 0"/><circle cx="14" cy="17" r="1.5" fill="#fff"/></svg>
    </div>
    <div class="status-time">9:41 AM</div>
    <div class="status-right">
      <svg width="14" height="22" viewBox="0 0 14 22" fill="none" stroke="#fff" stroke-width="2"><path d="M1 6l11 10-5 5V1l5 5L1 16"/></svg>
      <span>100%</span>
      <svg width="46" height="22" viewBox="0 0 46 22"><rect x="1" y="1" width="40" height="20" rx="5" fill="none" stroke="#fff" stroke-width="2"/><rect x="4" y="4" width="34" height="14" rx="3" fill="#fff"/><rect x="42" y="7" width="3" height="8" rx="1" fill="#fff"/></svg>
    </div>
  </div>

  <h1 class="header-title">KETO LEVELS</h1>
  <div class="header-icons">
    <svg width="26" height="24" viewBox="0 0 26 24" fill="#fff"><rect x="0" y="14" width="6" height="10"/><rect x="9" y="8" width="6" height="16"/><rect x="18" y="0" width="6" height="24" opacity="0.9"/></svg>
    <svg width="40" height="22" viewBox="0 0 40 22"><rect x="1.5" y="1.5" width="34" height="19" rx="5" fill="none" stroke="#fff" stroke-width="3"/><rect x="5" y="5" width="18" height="12" rx="2" fill="#fff"/><rect x="36" y="7" width="3" height="8" rx="1" fill="#fff"/></svg>
  </div>

  <div class="month-picker">
    <span>April 2018</span>
    <svg width="20" height="12" viewBox="0 0 20 12" fill="none" stroke="#111" stroke-width="2.4" stroke-linecap="round" stroke-linejoin="round"><path d="M2 2l8 8 8-8"/></svg>
  </div>

  <svg class="chart" width="750" height="400" viewBox="0 240 750 400" font-family="Montserrat, Arial, sans-serif">
    <defs>
      <linearGradient id="barFill" x1="0" y1="0" x2="0" y2="1">
        <stop offset="0" stop-color="var(--bar-top)"/>
        <stop offset="1" stop-color="var(--bar-bottom)"/>
      </linearGradient>
    </defs>
    <g fill="url(#barFill)">
      <rect x="16" y="287" width="20" height="273" rx="10"/>
      <rect x="46" y="348" width="20" height="212" rx="10"/>
      <rect x="76" y="400" width="20" height="160" rx="10"/>
      <rect x="106" y="376" width="20" height="184" rx="10"/>
      <rect x="136" y="455" width="20" height="105" rx="10"/>
      <rect x="166" y="478" width="20" height="82" rx="10"/>
      <rect x="196" y="395" width="20" height="165" rx="10"/>
      <rect x="226" y="348" width="20" height="212" rx="10"/>
      <rect x="256" y="390" width="20" height="170" rx="10"/>
      <rect x="286" y="304" width="20" height="256" rx="10"/>
      <rect x="316" y="433" width="20" height="127" rx="10"/>
      <rect x="346" y="412" width="20" height="148" rx="10"/>
      <rect x="376" y="369" width="20" height="191" rx="10"/>
      <rect x="406" y="394" width="20" height="166" rx="10"/>
      <rect x="438" y="287" width="20" height="273" rx="10"/>
      <rect x="468" y="348" width="20" height="212" rx="10"/>
      <rect x="498" y="400" width="20" height="160" rx="10"/>
      <rect x="528" y="376" width="20" height="184" rx="10"/>
      <rect x="558" y="455" width="20" height="105" rx="10"/>
      <rect x="588" y="478" width="20" height="82" rx="10"/>
      <rect x="618" y="395" width="20" height="165" rx="10"/>
      <rect x="648" y="348" width="20" height="212" rx="10"/>
      <rect x="678" y="390" width="20" height="170" rx="10"/>
      <rect x="708" y="304" width="20" height="256" rx="10"/>
      <rect x="738" y="433" width="20" height="127" rx="10"/>
    </g>
    <line x1="355" y1="288" x2="355" y2="560" stroke="#fff" stroke-width="2" stroke-dasharray="6 4"/>
    <text x="355" y="274" fill="#fff" font-size="18" font-weight="500" text-anchor="middle">0.6</text>
    <g fill="#fff" font-size="21" font-weight="400" text-anchor="middle">
      <text x="24" y="586">M</text><text x="55" y="586">T</text><text x="87" y="586">W</text><text x="117" y="586">T</text><text x="146" y="586">F</text><text x="177" y="586">S</text><text x="206" y="586">S</text>
      <text x="236" y="586">M</text><text x="266" y="586">T</text><text x="297" y="586">W</text><text x="328" y="586">T</text><text x="356" y="586">F</text><text x="387" y="586">S</text><text x="416" y="586">S</text>
      <text x="446" y="586">M</text><text x="477" y="586">T</text><text x="509" y="586">W</text><text x="539" y="586">T</text><text x="568" y="586">F</text><text x="599" y="586">S</text><text x="628" y="586">S</text>
      <text x="658" y="586">M</text><text x="688" y="586">T</text><text x="719" y="586">W</text><text x="750" y="586">T</text>
    </g>
    <g stroke="var(--icon-grey)" stroke-width="1.5">
      <line x1="22" y1="619" x2="78" y2="619"/><line x1="152" y1="619" x2="202" y2="619"/>
      <line x1="237" y1="619" x2="292" y2="619"/><line x1="366" y1="619" x2="416" y2="619"/>
      <line x1="451" y1="619" x2="506" y2="619"/><line x1="580" y1="619" x2="630" y2="619"/>
      <line x1="665" y1="619" x2="720" y2="619"/>
    </g>
    <g fill="#fff" font-size="15" font-weight="700" text-anchor="middle">
      <text x="115" y="624">WEEK 1</text>
      <text x="330" y="624">WEEK 2</text>
      <text x="544" y="624">WEEK 3</text>
      <text x="728" y="624" text-anchor="start">WEEK 4</text>
    </g>
  </svg>

  <div class="latest-row">
    <svg class="drop-icon" width="24" height="32" viewBox="0 0 24 32"><path d="M12 1C8 9 2 15 2 21a10 10 0 0 0 20 0C22 15 16 9 12 1z" fill="var(--icon-grey)"/></svg>
    <span class="latest-label">LATEST KETO LEVEL</span>
    <span class="latest-value">0.6 mmol/L</span>
  </div>

  <svg class="start-test" viewBox="0 0 240 240" aria-label="Start keto test">
    <defs>
      <linearGradient id="playFill" x1="0" y1="0" x2="0" y2="1">
        <stop offset="0" stop-color="var(--bar-top)"/>
        <stop offset="1" stop-color="var(--bar-bottom)"/>
      </linearGradient>
    </defs>
    <circle cx="120" cy="120" r="120" fill="url(#playFill)"/>
    <path d="M97 93q0-8 7-4l55 29q6 3 0 6l-55 29q-7 4-7-4z" fill="#fff"/>
  </svg>
  <div class="start-label">START KETO TEST</div>

  <nav class="tab-bar">
    <div class="tab">
      <svg viewBox="0 0 34 34" fill="none" stroke="currentColor" stroke-width="2.2" stroke-linecap="round" stroke-linejoin="round"><path d="M3 15l7-7 6 6 6-7 8 6"/><path d="M3 24l7-7 6 6 6-7 8 6"/></svg>
      <span>Activity</span>
    </div>
    <div class="tab">
      <svg viewBox="0 0 34 34" fill="none" stroke="currentColor" stroke-width="2.2"><rect x="4" y="4" width="5" height="5"/><rect x="4" y="14" width="5" height="5"/><rect x="4" y="24" width="5" height="5"/><path d="M14 6h16M14 16h16M14 26h16"/></svg>
      <span>Health Data</span>
    </div>
    <div class="tab is-active">
      <svg viewBox="0 0 34 34" fill="none" stroke="currentColor" stroke-width="2.2" stroke-linecap="round"><circle cx="17" cy="17" r="14"/><path d="M17 17l6-6"/><path d="M17 7v2M7 17h2M25 17h2M10 10l1.5 1.5M10 24l1.5-1.5M24 24l-1.5-1.5"/></svg>
      <span>Keto Test</span>
    </div>
    <div class="tab">
      <svg viewBox="0 0 34 34" fill="none" stroke="currentColor" stroke-width="2.2"><circle cx="17" cy="11" r="7"/><path d="M4 32c0-8 6-12 13-12s13 4 13 12z"/></svg>
      <span>Your Info</span>
    </div>
    <div class="tab">
      <svg viewBox="0 0 34 34" fill="none" stroke="currentColor" stroke-width="2.2" stroke-linejoin="round"><path d="M14 2h6l1 4 4 2 4-2 3 5-3 3v4l3 3-3 5-4-2-4 2-1 4h-6l-1-4-4-2-4 2-3-5 3-3v-4l-3-3 3-5 4 2 4-2z"/><circle cx="17" cy="17" r="5"/></svg>
      <span>Settings</span>
    </div>
  </nav>
</div>
</body>
</html>
```